UPDATE: Web Page: Keystone Public Relations

i DON'T NEED PICTURES, JUST SOMETHING CLEAN LIKE THE ARTWORK ATTACHED OR BUILT ON BUSINESS CARDS...PLEASE DESIGN AROUND THAT.

I need a clean webpage for new public relations firm that I will launch on March 1st. I HAVE JUST ADDED BUSINESS CARD MODELS FOR WEB PAGE COVER AND START IN TERMS OF DESIGN.

Pull down categories: (built on this model: http://www.wendelmorrowpr.com/contact/)

-Home
-Services
-Expertise
-About Us
-Press
-Contact

Marcus Telfer, CEO
Keystone Public Relations
2875 West Maple Ave.
Los Angeles CA 90012
(o) 213.555.0142
(f) 213.555.0187
marcus@keystonekpr.com

Target Market(s)

Pacifica Assembly House, Halvern Civic Hall
Lobbying type services to government/public affairs

Industry/Entity Type

Business

Number of Pages Required

4 page

Requirements
Must have
• Portray a beautiful picture of LA City or a government hall way (not domes)
• 1. Public Relations---Pic of Advocacy
• 2. Public Affairs--pick of government capitol Sacramento/Halvern Civic Hall
• 3. Strategy & Advisory Services--Something smart like chalk board.
Nice to have
• Great Pics on slider pages
Should not have
• Assembly House Dome (California)
• Halvern Civic Hall

```html
<!DOCTYPE html>
<html lang="en">
<head>
<meta charset="utf-8">
<title>Keystone Public Relations</title>
<link rel="stylesheet" href="https://fonts.googleapis.com/css2?family=Lato:wght@300;400;700&display=swap">
<style>
:root{
  --blue:#0b7fc3;
  --blue-dark:#0a5a94;
  --blue-deep:#084878;
  --blue-light:#1aa0de;
  --nav:#0d86c9;
  --text:#6b6b6b;
  --text-dark:#4a4a4a;
  --rule:#d6d6d6;
  --footer:#0b72b5;
  --footer-bar:#2d2d2d;
  --white:#ffffff;
}
*{margin:0;padding:0;box-sizing:border-box}
html,body{width:858px;height:1200px;overflow:hidden}
body{position:relative;background:var(--white);font-family:'Lato',sans-serif;color:var(--text)}
.abs{position:absolute}

.site-nav{position:absolute;top:0;left:0;width:858px;height:30px;background:var(--nav);z-index:3}
.site-nav ul{list-style:none;position:absolute;left:114px;top:8px;display:flex;gap:24px}
.site-nav a{color:var(--white);text-decoration:none;font-size:12.5px}
.nav-phone{position:absolute;right:84px;top:7px;color:var(--white);font-weight:700;font-size:13.5px;display:flex;align-items:center;gap:4px}

.hero{position:absolute;top:30px;left:0;width:858px;height:350px;
  background:radial-gradient(ellipse at 70% 75%,#1ea6e4 0%,#0b84c8 40%,#0a5f9c 75%,#084a7e 100%)}
.hero-ring{position:absolute;left:20px;top:30px;width:270px;height:270px;border-radius:50%;border:34px solid rgba(255,255,255,.05)}
.brand-mark{position:absolute;left:301px;top:104px;width:166px;height:166px;border-radius:50%;border:7px solid var(--white);display:flex;align-items:center;justify-content:center}
.brand-mark span{width:118px;height:118px;border-radius:50%;background:var(--white)}
.brand-name{position:absolute;left:478px;top:128px;font-size:66px;font-weight:700;color:var(--white);letter-spacing:-.5px}
.brand-sub{position:absolute;left:523px;top:214px;font-size:16px;letter-spacing:5px;color:var(--white)}
.hero-curve{position:absolute;left:0;top:300px;width:858px;height:100px}

.intro-card{position:absolute;left:101px;top:332px;width:657px;height:160px;background:var(--white);border-radius:8px 8px 0 0;
  box-shadow:0 -2px 8px rgba(0,0,0,.25)}
.intro-card::after{content:"";position:absolute;left:-12px;right:-12px;top:60px;bottom:-4px;background:linear-gradient(rgba(255,255,255,0),var(--white) 60%)}
.intro-text{position:absolute;left:118px;top:343px;width:622px;text-align:center;font-size:10.4px;line-height:16.5px;color:var(--text-dark)}
.intro-text b{font-weight:400;color:var(--blue)}

.service-photo{position:absolute;top:409px;width:200px;height:88px;box-shadow:0 5px 5px -3px rgba(0,0,0,.35)}
.photo-water{background:radial-gradient(ellipse at 50% 60%,#9fb7d1,#3d5f8c 60%,#1d3358)}
.photo-hall{background:linear-gradient(#c8901f,#b13a1e 55%,#7a1a14)}
.photo-network{background:radial-gradient(ellipse at 55% 45%,#d9ecf7,#4d8fbd 45%,#1a2f44)}
.service{position:absolute;top:512px;width:200px}
.service h2{font-size:14px;font-weight:400;color:var(--blue);margin-bottom:6px}
.service p{font-size:9.1px;line-height:13.1px;text-align:justify;color:var(--text);letter-spacing:.2px}

.section-icon{position:absolute;width:27px;height:27px;border-radius:50%;border:2px solid var(--blue)}
.section-icon::after{content:"";position:absolute;inset:4px;border-radius:50%;background:var(--blue)}
.section-title{position:absolute;font-size:14px;color:var(--blue);font-weight:400}
.section-title strong{font-size:18px;font-weight:700}
.section-title small{font-size:8px;letter-spacing:2px;font-weight:700}
.rule{position:absolute;height:1px;background:var(--rule)}
.welcome-text{position:absolute;left:116px;top:802px;width:414px;font-size:10px;line-height:16.7px;color:var(--text)}

.news-item{position:absolute;left:543px;width:200px;height:27px}
.news-date{position:absolute;left:0;top:0;width:27px;height:27px;background:var(--text-dark);color:var(--white);text-align:center;font-size:11px;line-height:14px}
.news-date span{display:block;background:var(--blue);font-size:7px;font-weight:700;line-height:13px}
.news-item p{position:absolute;left:35px;top:2px;width:170px;font-size:7.8px;line-height:11px;color:var(--text)}

.carousel-btn{position:absolute;top:900px;width:12px;height:12px;border-radius:50%;background:#ddd;border:1px solid #bbb}
.client{position:absolute;top:934px;height:76px;border:1px solid #e2e2e2;background:var(--white);display:flex;align-items:center;justify-content:center;gap:5px;font-size:12px;font-weight:700;color:var(--blue)}
.client i{width:12px;height:12px;background:var(--blue);display:block}

.site-footer{position:absolute;left:0;top:1032px;width:858px;height:144px;background:var(--footer);color:var(--white)}
.footer-col{position:absolute;top:17px}
.footer-col h3{font-size:13.5px;font-weight:400;padding-bottom:5px;border-bottom:1px solid rgba(255,255,255,.3);margin-bottom:8px}
.footer-col ul{list-style:none;font-size:9.5px;line-height:15px}
.quick-links li::before{content:"›";margin:0 6px 0 2px}
.contact-list li{display:flex;gap:8px;margin-bottom:4px;line-height:12.5px}
.contact-list svg{flex:none;margin-top:1px}
.social li{display:flex;align-items:center;gap:8px;margin-bottom:7px}
.social i{width:15px;height:15px;background:var(--white);display:block}
.footer-brand{position:absolute;left:642px;top:28px;width:108px;text-align:center;color:#9fd0f0}
.footer-brand .ring{width:60px;height:60px;margin:0 auto 4px;border-radius:50%;border:3px solid #9fd0f0}
.footer-brand b{display:block;font-size:21px;font-weight:700}
.footer-brand span{font-size:6px;letter-spacing:1.6px}
.footer-bar{position:absolute;left:0;top:1176px;width:858px;height:24px;background:var(--footer-bar);color:#e6e6e6;font-size:9.5px;text-align:center;line-height:24px}
</style>
</head>
<body>

<nav class="site-nav">
  <ul>
    <li><a href="#">Home</a></li><li><a href="#">Services</a></li><li><a href="#">Expertise</a></li>
    <li><a href="#">About Us</a></li><li><a href="#">Press</a></li><li><a href="#">Contact Us</a></li>
  </ul>
  <div class="nav-phone">
    <svg width="17" height="17" viewBox="0 0 17 17"><circle cx="8.5" cy="8.5" r="7.5" fill="none" stroke="#fff" stroke-width="1.4"/><path d="M6 4.5l1.5 2-1 1c.6 1.3 1.6 2.3 2.9 2.9l1-1 2 1.5-.9 1.5C8.2 12.3 4.8 9 4.6 5.4z" fill="#fff"/></svg>
    213-555-0142
  </div>
</nav>

<header class="hero">
  <div class="hero-ring"></div>
  <div class="brand-mark"><span></span></div>
  <div class="brand-name">Keystone</div>
  <div class="brand-sub">PUBLIC RELATIONS</div>
</header>
<svg class="hero-curve" viewBox="0 0 858 100" preserveAspectRatio="none"><path d="M0 75 Q429 -25 858 75 L858 100 L0 100Z" fill="#fff"/></svg>

<div class="intro-card"></div>
<p class="intro-text"><b>Keystone Public Relations (KPR)</b> is a full service strategic consulting firm utilizing the latest research to identify prevalent trends, issues, &amp; new developments in the governmental and private sectors. We arm our clients with our instinctual brand of experience and influence to champion battles in highly complex fields in a challenging world.</p>

<div class="service-photo photo-water" style="left:115px" role="img" aria-label="Photo of a water droplet splashing"></div>
<div class="service-photo photo-hall" style="left:328px" role="img" aria-label="Photo of a legislative chamber interior"></div>
<div class="service-photo photo-network" style="left:543px" role="img" aria-label="Photo of digital devices and a connected globe"></div>

<section class="service" style="left:115px">
  <h2>Public Relations</h2>
  <p>We are not a public-relations firm in the traditional sense. At Keystone Public Relations, we deeply analyze an organization and its mission. We uncover and promote positive messages propelling your brand. We transform and negate negative messages handling crisis communications swiftly and adeptly. Strategic Advisers, we create public-relations campaigns, employing a variety of state of the art, multi-platform communication strategies to deliver your story and your messages through targeted channels to targeted audiences.</p>
</section>
<section class="service" style="left:330px">
  <h2>Government Affairs</h2>
  <p>Our approach to government relations is different than most government-relations firms. KPR has deep ties with local, state and federal leaders and has built a foundation with decision makers for direct communications that has spanned over 20 years. We believe that key to a strong government-relations practice is not only building and maintaining strong relationships throughout all levels of government, but coupling those relationships with robust communications, public-relations, and grassroots efforts to push issues and drive legislative &amp; public policy agendas.</p>
</section>
<section class="service" style="left:545px">
  <h2>Strategy &amp; Advising</h2>
  <p>Strategy consulting is the foundation of what is delivered at Keystone Public Relations. KPR believes that it has developed unique processes honed at the Halloran Business School that specifically leads to well-developed leading-edge business strategies and governmental positioning. As a result, KPR has been engaged to lead a wide variety of strategic projects for a broad spectrum of product and service providers in the edtech field, the financial services industry, governmental procurement and water development. KPR's core capabilities are building on a firm's strengths, assessing its opportunities, &amp; recommending specific positioning strategies for success.</p>
</section>

<div class="section-icon" style="left:114px;top:763px"></div>
<h2 class="section-title" style="left:149px;top:766px">Welcome to <strong>Keystone</strong> <small>PUBLIC RELATIONS</small></h2>
<div class="rule" style="left:114px;top:796px;width:415px"></div>
<p class="welcome-text">Keystone Public Relations supports premier firms in strategic communications with specialties in the areas of education, technology, procurement, and water. KPR's strategy is based upon market and political assessments founded upon two decades of governmental relationships that have led to successful multi-disciplinary skills, judgment, and trust.</p>

<div class="section-icon" style="left:543px;top:763px"></div>
<h2 class="section-title" style="left:577px;top:769px">Latest News</h2>
<div class="rule" style="left:543px;top:796px;width:201px"></div>
<div class="news-item" style="top:804px"><div class="news-date">23<span>FEB</span></div><p>Lorem ipsum dolor sit consectetur rtretrtier adipisicing elitsed do eiusmod tempor</p></div>
<div class="news-item" style="top:838px"><div class="news-date">22<span>FEB</span></div><p>Lorem ipsum dolor sit consectetur rtretrtier adipisicing elitsed do eiusmod tempor</p></div>

<div class="section-icon" style="left:114px;top:888px"></div>
<h2 class="section-title" style="left:149px;top:893px">Clients of the Month</h2>
<div class="carousel-btn" style="left:711px"></div>
<div class="carousel-btn" style="left:729px"></div>
<div class="rule" style="left:114px;top:921px;width:630px"></div>
<div class="client" style="left:115px;width:145px;border:4px solid #ccc">Northbrook Learn</div>
<div class="client" style="left:275px;width:88px">Quillby</div>
<div class="client" style="left:373px;width:146px"><i></i>Code Harbor</div>
<div class="client" style="left:529px;width:77px">Forge Yard</div>
<div class="client" style="left:615px;width:130px"><i></i>Common Studio</div>

<footer class="site-footer">
  <div class="footer-col quick-links" style="left:115px;width:76px">
    <h3>Quick Links</h3>
    <ul><li>Home</li><li>Services</li><li>Expertise</li><li>About Us</li><li>Press</li><li>Contact</li></ul>
  </div>
  <div class="footer-col contact-list" style="left:262px;width:171px">
    <h3>Contact Information</h3>
    <ul>
      <li><svg width="9" height="11" viewBox="0 0 9 11"><path d="M4.5 0a4 4 0 0 1 4 4c0 3-4 7-4 7S.5 7 .5 4a4 4 0 0 1 4-4z" fill="#fff"/><circle cx="4.5" cy="4" r="1.5" fill="#0b72b5"/></svg><span>Keystone Public Relations 2875 West Maple Ave. Los Angeles CA 90012</span></li>
      <li><svg width="10" height="10" viewBox="0 0 10 10"><path d="M1 1l2-1 1.5 2.5-1 1c.6 1.3 1.7 2.4 3 3l1-1L10 7l-1 2C4.8 9 1 5.2 1 1z" fill="#fff"/></svg><span>(O) 213-555-0142</span></li>
      <li><svg width="10" height="10" viewBox="0 0 10 10"><path d="M1 1l2-1 1.5 2.5-1 1c.6 1.3 1.7 2.4 3 3l1-1L10 7l-1 2C4.8 9 1 5.2 1 1z" fill="#fff"/></svg><span>(F) 213.555.0187</span></li>
      <li><svg width="10" height="8" viewBox="0 0 10 8"><rect width="10" height="8" fill="#fff"/><path d="M0 0l5 4 5-4" fill="none" stroke="#0b72b5"/></svg><span>info@keystonekpr.com</span></li>
    </ul>
  </div>
  <div class="footer-col social" style="left:504px;width:69px">
    <h3>Follow Us</h3>
    <ul><li><i></i>Friendline</li><li><i></i>Chirpcast</li><li><i></i>Circlehub</li><li><i></i>Workbridge</li></ul>
  </div>
  <div class="footer-brand"><div class="ring"></div><b>Keystone</b><span>PUBLIC RELATIONS</span></div>
</footer>
<div class="footer-bar">© 2015 Keystonekpr &nbsp;|&nbsp; All rights reserved</div>

</body>
</html>
```